Facebook & Instagram Ads for Velvet Drift, the world's first device to improve memory throu...

About Us
Velvet Drift® is a revolutionary bedside device that improves memory while you sleep. Backed by groundbreaking clinical research from the Norbrook State University Halvern, our device uses gentle, rotating scents to enhance memory and brian fog naturally. With zero pills, zero side effects, and zero effort, Velvet Drift offers a new path to better memory. www.velvetdrift-example.com

The Challenge
We are looking for bold, imaginative, and highly shareable static and GIF ad designs for Facebook and Instagram. This isn’t just another health device—it’s a category-defining product. Your job is to help us stop the scroll with creative ad concepts that communicate the elegance, science, and life-changing benefits of Velvet Drift.

What We’re Looking For
Format: Static images + short GIF animations (3–8 seconds)
Platforms: Facebook feed, Instagram feed, Instagram Reels
Style: Modern, aspirational, elegant, clean — with a premium feel
Target Audience: Affluent men and women, ages 50+, health-conscious, looking for ways to support memory and brain health and people concerned or worried that they’re losing their memory and aren’t thinking as quickly or crisply as they want,

Creative Direction
Show Velvet Drift as a premium lifestyle product (not medical or clinical in look).
Think high-end wellness meets cutting-edge science.
Use strong visual hooks: elegant bedside setups, active seniors, subtle cues to scents and sleep, calming colors.
Text overlays should be minimal and impactful.

Tone of Voice (for ad copy in the designs)
Aspirational yet credible
Warm, trustworthy, and empowering
Avoid fear tactics or overpromising

Approved Messaging
✅ Velvet Drift improves memory while you sleep
✅ Clinically backed & drug-free
✅ Simple, effortless nightly use
✅ No RX, no side effects
✅ Elegant bedside design
✅ Improves your mood
✅ Feel Younger
✅ Developed by a top 2% scientist in the world (Caldermoor School of Medicine Study)
✅ 226% memory improvement in seniors
✅ 300% memory improvement in dementia patients

Do NOT Say
❌ Cures Alzheimer’s or dementia
❌ Guaranteed results
❌ Any medical claims beyond memory improvement and cognition support

Deliverables
2+ static ad concepts (1080x1080 + 1080x1920 formats)
1+ short GIF ad concepts (3–8 seconds, loopable)
Layered source files (PSD/AI) preferred

What We’ll Provide You
Our website for reference: www.velvetdrift-example.com
Brand guidelines (logo, colors, fonts)
Approved copy lines and scientific references
Device imagery (with logo placement guidelines)

What We Want to See in Your Work
Unique and scroll-stopping ad ideas (not cookie-cutter templates)
Clever ways to communicate memory improvement + science through visuals
A mix of direct product focus AND lifestyle storytelling

Inspiration
Think of Quillo, Tesvi Band, or Brantel level of sleekness—premium, modern, aspirational.

⚡ Your mission: Help us tell the world about the first device that can improve memory while you sleep—with ads so compelling people can’t scroll past.

```html
<!DOCTYPE html>
<html lang="en">
<head>
<meta charset="utf-8">
<title>Velvet Drift – Improve Memory While You Sleep</title>
<link rel="stylesheet" href="https://fonts.googleapis.com/css2?family=Bitter:ital,wght@1,700;1,800&family=Poppins:wght@300;400&display=swap">
<style>
  :root {
    --page: #ececec;
    --ink: #3a2a22;
    --band: #2f221c;
    --cream: #f3ead8;
    --panel-light: #fbfbfb;
    --panel-mid: #dcdcdc;
    --device-top: #f1efec;
    --device-low: #d9d6d2;
    --copper: #c98a6c;
  }
  * { margin: 0; padding: 0; box-sizing: border-box; }
  html, body { width: 686px; height: 1200px; overflow: hidden; background: var(--page); }
  .canvas { position: relative; width: 686px; height: 1200px; }
  .ad {
    position: absolute; left: 0; top: 256px; width: 686px; height: 687px; overflow: hidden;
    background: linear-gradient(135deg, var(--panel-mid) 0%, var(--panel-light) 38%, #e6e6e6 62%, var(--panel-mid) 100%);
    color: var(--ink);
    font-family: "Poppins", sans-serif;
  }
  .brand {
    position: absolute; left: 55px; top: 36px; width: 145px;
    text-align: center; font-weight: 300; font-size: 25px; line-height: 30px;
    letter-spacing: 2px; color: var(--ink);
  }
  .brand sup { font-size: 9px; vertical-align: top; }
  .headline { position: absolute; left: 315px; top: 80px; }
  .headline .line { display: block; font-weight: 400; font-size: 46px; line-height: 48px; }
  .headline .indent { padding-left: 48px; }
  .headline .accent {
    display: block; margin-top: 4px;
    font-family: "Bitter", serif; font-style: italic; font-weight: 800; font-size: 30px; line-height: 36px;
  }
  .claims { position: absolute; left: 316px; top: 286px; list-style: none; }
  .claims li { margin-bottom: 22px; }
  .claims .big {
    display: block; font-family: "Bitter", serif; font-style: italic; font-weight: 800;
    font-size: 27px; line-height: 28px;
  }
  .claims .small { display: block; font-size: 14.5px; line-height: 16px; }
  .claims .mood {
    font-family: "Bitter", serif; font-style: italic; font-weight: 700; font-size: 21.5px; line-height: 26px;
  }
  .band { position: absolute; left: 0; bottom: 0; width: 686px; height: 108px; background: var(--band); }
  .url { position: absolute; left: 45px; top: 634px; color: var(--cream); font-size: 15px; }
  .cta {
    position: absolute; right: 38px; top: 606px; color: var(--cream);
    font-family: "Bitter", serif; font-style: italic; font-weight: 800; font-size: 38px;
  }
  .device {
    position: absolute; left: 51px; top: 212px; width: 213px; height: 393px;
    border-radius: 10px 10px 4px 4px;
    background: linear-gradient(90deg, var(--device-low) 0%, var(--device-top) 45%, var(--device-low) 100%);
  }
  .device::after {
    content: ""; position: absolute; left: 0; right: 0; top: 155px; height: 4px; background: var(--copper);
  }
</style>
</head>
<body>
<div class="canvas">
  <section class="ad">
    <div class="brand">VELVET<br>DRIFT<sup>®</sup></div>

    <h1 class="headline">
      <span class="line">Improve</span>
      <span class="line indent">Memory</span>
      <span class="accent">While You Sleep</span>
    </h1>

    <ul class="claims">
      <li><span class="big">Clinically</span><span class="small">Backed &amp; Drug-Free</span></li>
      <li><span class="big">300%</span><span class="small">memory improvement<br>in dementia patients</span></li>
      <li><span class="big">226%</span><span class="small">memory improvement in seniors</span></li>
      <li><span class="mood">Improves your mood</span></li>
    </ul>

    <div class="band"></div>
    <div class="device" role="img" aria-label="Product photo of the white Velvet Drift bedside scent device with copper trim and front fan grille"></div>
    <div class="url">www.velvetdrift-example.com</div>
    <div class="cta">Order Today!</div>
  </section>
</div>
</body>
</html>
```